Korvatch Law Rebrand

I am recreating my law firm website. I got a new logo and would like to recreate the website to match the new logo. the website is korvatchlaw.com

```html
<!DOCTYPE html>
<html lang="en">
<head>
<meta charset="utf-8">
<title>Korvatch Law, PLLC</title>
<link rel="stylesheet" href="https://fonts.googleapis.com/css2?family=Poppins:wght@300;400;500;600;700&family=Oswald:wght@500;600&display=swap">
<style>
:root{
  --navy:#0c4f92;
  --navy-dark:#0a437d;
  --slate:#9aa8c4;
  --slate-text:#8d9cb9;
  --ink:#222831;
  --field:#f1f1f1;
  --card:#f4f4f4;
  --white:#ffffff;
}
*{box-sizing:border-box;margin:0;padding:0}
html,body{width:1200px;height:5017px;overflow:hidden}
body{position:relative;background:var(--white);font-family:"Poppins",sans-serif;color:var(--ink)}
.abs{position:absolute}
.photo{position:absolute}

/* header */
.brand{left:80px;top:34px;font-size:22px;font-weight:600;letter-spacing:3px;color:var(--navy)}
.nav{left:334px;top:52px;display:flex;gap:38px;font-size:12px;font-weight:500;letter-spacing:.3px}
.nav a{color:var(--ink);text-decoration:none}
.nav a.active{color:var(--navy)}
.btn-head{left:744px;top:34px;width:209px;height:42px;background:var(--navy);color:#fff;font-size:12px;font-weight:500;display:flex;align-items:center;justify-content:center}
.phone-head{left:963px;top:34px;width:170px;height:42px;background:var(--slate);color:#fff;font-size:13px;display:flex;align-items:center;justify-content:center;gap:10px}
.phone-head .dot{width:22px;height:22px;border-radius:50%;background:#fff;display:flex;align-items:center;justify-content:center}

/* hero */
.hero{left:0;top:107px;width:1200px;height:706px;overflow:hidden}
.hero-text{right:58px;top:185px;text-align:right;color:#fff}
.hero-welcome{font-size:22px;font-weight:300;letter-spacing:1px;color:#d7e2f0}
.hero-title{font-family:"Oswald",sans-serif;font-weight:600;font-size:88px;line-height:1.05;margin-top:18px;letter-spacing:1px}
.hero-sub{font-size:26px;font-weight:300;line-height:44px;margin-top:22px}
.btn-hero{right:58px;top:607px;width:336px;height:61px;background:var(--slate);color:#fff;font-size:21px;font-weight:500;display:flex;align-items:center;justify-content:center;border-radius:3px}

/* services */
.service{top:858px;width:200px;text-align:center}
.service .icon{width:92px;height:92px;margin:0 auto;border:2px solid #c9d6e6;border-radius:6px;padding:5px}
.service .icon span{display:block;width:100%;height:100%;background:var(--navy);border-radius:3px}
.service h3{margin-top:16px;font-size:18px;font-weight:600;color:var(--navy);line-height:23px}

/* about */
.about-frame{left:107px;top:1148px;width:386px;height:405px;background:#e4e4e4;border-radius:4px;overflow:hidden}
.about-frame .inner{position:absolute;left:14px;top:14px;right:14px;bottom:14px;border:2px solid #fff;border-radius:6px}
.bar{width:3px;background:var(--navy)}
.about-head{left:596px;top:1165px}
.about-title{left:618px;top:1152px;font-size:44px;font-weight:500;color:var(--navy);letter-spacing:.5px}
.about-title span{color:var(--slate-text)}
.about-kicker{left:626px;top:1208px;font-size:22px;color:var(--slate-text)}
.about-copy{left:595px;top:1275px;width:470px;font-size:13px;line-height:24px;color:#333}
.about-copy p+p{margin-top:24px}
.btn-navy{background:var(--navy);color:#fff;font-size:12px;font-weight:500;display:flex;align-items:center;justify-content:center;border-radius:3px}
.btn-slate{background:var(--slate);color:#fff;font-size:12px;font-weight:500;display:flex;align-items:center;justify-content:center;border-radius:3px}

/* practices */
.pa-panel{left:0;top:1760px;width:404px;height:710px;background:var(--navy)}
.pa-notch{left:402px;top:2060px}
.pa-bar{left:68px;top:1862px;height:98px;background:#fff;width:3px}
.pa-title{left:88px;top:1852px;font-size:46px;font-weight:500;color:#fff;line-height:58px;letter-spacing:1px}
.pa-copy{left:88px;top:2012px;width:276px;font-size:13px;line-height:26.6px;color:#fff;text-align:justify}
.pa-btn{left:90px;top:2330px;width:262px;height:96px;background:var(--slate);color:#fff;font-size:23px;font-weight:500;line-height:30px;text-align:center;display:flex;align-items:center;justify-content:center;border-radius:3px}
.pa-card{width:316px;height:343px;overflow:hidden}
.pa-label{position:absolute;left:20px;bottom:0;width:276px;height:82px;background:var(--navy);color:#fff;padding:16px 22px;font-size:24px;font-weight:600;line-height:30px}
.pa-label .go{position:absolute;right:16px;top:27px;width:30px;height:30px;border-radius:50%;background:#9fb2cc;display:flex;align-items:center;justify-content:center}

/* blog */
.blog-bar{left:68px;top:2672px;height:74px}
.blog-title{left:86px;top:2660px;font-size:48px;font-weight:500;color:var(--navy);letter-spacing:1px}
.blog-kicker{left:86px;top:2722px;font-size:23px;color:var(--slate-text)}
.arrow{width:58px;height:58px;border-radius:50%;display:flex;align-items:center;justify-content:center}
.post{top:2822px;width:324px;height:443px;background:var(--card);border-bottom:5px solid var(--navy)}
.post .img{height:222px}
.post .meta{margin:22px 0 0 10px;font-size:11px;color:#444;display:flex;align-items:center;gap:6px}
.post .meta i{width:13px;height:13px;background:var(--navy);display:block}
.post h4{margin:14px 10px 0;font-size:21px;font-weight:500;color:var(--navy);line-height:24px}
.post p{margin:10px 10px 0;font-size:13px;line-height:20px;color:#333}
.post .more{position:absolute;left:10px;top:374px;padding:9px 14px;border:2px solid var(--navy);color:var(--navy);font-size:12px;font-weight:600;border-radius:3px}

/* schedule */
.sch-bar{left:68px;top:3505px;height:96px}
.sch-title{left:90px;top:3490px;font-size:41px;font-weight:500;color:var(--navy);line-height:52px;letter-spacing:.5px}
.field{background:var(--field);font-size:13px;color:#444;padding:14px 22px}
.sch-photo{left:777px;top:3557px;width:363px;height:406px;border-radius:4px;overflow:hidden}
.sch-photo .inner{position:absolute;left:12px;top:12px;right:12px;bottom:12px;border:2px solid #e9e2d8;border-radius:6px}

/* newsletter */
.news-title{left:0;top:4240px;width:1200px;text-align:center;font-size:46px;font-weight:500;color:var(--navy);letter-spacing:1px}
.news-sub{left:0;top:4344px;width:1200px;text-align:center;font-size:18px;font-weight:500}
.news-box{left:225px;top:4403px;width:773px;height:69px;border:2px solid #d9d9d9;border-radius:36px}
.news-box .ph{position:absolute;left:38px;top:22px;font-size:15px;font-weight:500}
.news-box .go{position:absolute;right:8px;top:11px;width:148px;height:44px;border-radius:22px;background:var(--navy);color:#fff;font-size:16px;font-weight:500;display:flex;align-items:center;justify-content:center}

/* footer */
.footer{left:0;top:4628px;width:1200px;height:332px;background:var(--navy);color:#fff}
.footer-rule{position:absolute;top:115px;height:1px;background:#3d72aa}
.f-head{position:absolute;top:80px;font-size:17px;font-weight:500}
.f-links{position:absolute;left:250px;top:140px;list-style:none;font-size:13px}
.f-links li{height:32px;display:flex;align-items:center;gap:8px}
.f-links li::before{content:"";width:6px;height:6px;border-right:2px solid #cfdbea;border-bottom:2px solid #cfdbea;transform:rotate(-45deg)}
.f-brand{position:absolute;left:0;width:1200px;top:158px;text-align:center;font-size:28px;font-weight:600;letter-spacing:4px}
.f-contact{position:absolute;left:838px;top:136px;font-size:12px;line-height:15px}
.f-contact .row{display:flex;gap:18px;margin-bottom:18px}
.f-contact .ic{width:26px;height:26px;border:1.5px solid #fff;border-radius:3px;display:flex;align-items:center;justify-content:center;flex:none}
.copyright{left:0;top:4960px;width:1200px;height:57px;background:var(--slate);color:#fff;font-size:12px;display:flex;align-items:center;justify-content:center}
</style>
</head>
<body>

<!-- header -->
<div class="abs brand">KORVATCH LAW</div>
<nav class="abs nav">
  <a class="active" href="#">HOME</a><a href="#">PRACTICES AREAS</a><a href="#">ABOUT ME</a><a href="#">BLOG</a>
</nav>
<div class="abs btn-head">SCHEDULE A CONSULTATION</div>
<div class="abs phone-head"><span class="dot"><svg width="12" height="12" viewBox="0 0 24 24"><path fill="#9aa8c4" d="M6.6 10.8a15 15 0 0 0 6.6 6.6l2.2-2.2c.3-.3.7-.4 1-.2 1.1.4 2.3.6 3.6.6.6 0 1 .4 1 1V20c0 .6-.4 1-1 1A17 17 0 0 1 3 4c0-.6.4-1 1-1h3.5c.6 0 1 .4 1 1 0 1.3.2 2.5.6 3.6.1.3 0 .7-.2 1z"/></svg></span>(555) 014-2290</div>

<!-- hero -->
<section class="abs hero">
  <div class="photo" role="img" aria-label="Photo of a lawyer in a suit leaning over a desk beside a brass scale of justice" style="left:0;top:0;width:1200px;height:706px;background:linear-gradient(120deg,#e8e8e6 0%,#cfcfcc 45%,#a88a66 80%)"></div>
  <svg class="abs" style="left:0;top:0" width="1200" height="706"><polygon points="730,0 1200,0 1200,706 487,706" fill="#0f569c"/></svg>
  <div class="abs hero-text">
    <div class="hero-welcome">WELCOME TO</div>
    <div class="hero-title">KORVATCH LAW</div>
    <div class="hero-sub">PERSONAL LEGAL SOLUTIONS<br>IN LIFE'S MOST DIFFICULT<br>MOMENTS</div>
  </div>
</section>
<div class="abs btn-hero">SCHEDULE A CONSULTATION</div>

<!-- services -->
<div class="abs service" style="left:168px"><div class="icon"><span role="img" aria-label="Probate document icon"></span></div><h3>PROBATE AND<br>TRUSTS</h3></div>
<div class="abs service" style="left:393px"><div class="icon"><span role="img" aria-label="Guardianship hands icon"></span></div><h3>ADULT<br>GUARDIANSHIPS</h3></div>
<div class="abs service" style="left:620px"><div class="icon"><span role="img" aria-label="Estate house icon"></span></div><h3>ESTATE<br>PLANNING</h3></div>
<div class="abs service" style="left:844px"><div class="icon"><span role="img" aria-label="Litigation gavel icon"></span></div><h3>CIVIL<br>LITIGATION</h3></div>

<!-- about -->
<div class="abs about-frame" role="img" aria-label="Portrait of the attorney in a dark suit and red tie" style="background:linear-gradient(180deg,#ececec 0%,#d8d8d8 55%,#1d2433 56%,#151b27 100%)"><div class="inner"></div></div>
<div class="abs bar" style="left:596px;top:1168px;height:64px"></div>
<div class="abs about-title">KORVATCH LAW, <span>PLLC</span></div>
<div class="abs about-kicker">ABOUT ME</div>
<div class="abs about-copy">
  <p>It is my honor to provide quality legal services at a reasonable price to clients that I enjoy working with and for. I am grateful for all my clients and the trust they place in me to represent them.</p>
  <p>My practice focuses on Probate, Adult Guardianships, and Trust Administration and Litigation. I also represent clients in other general civil litigation matters. Finally, I handle estate planning for families of modest means.</p>
</div>
<div class="abs btn-navy" style="left:595px;top:1507px;width:155px;height:46px">KNOW MORE</div>
<div class="abs btn-slate" style="left:762px;top:1507px;width:244px;height:46px">SCHEDULE A CONSULTATION</div>

<!-- practices -->
<div class="abs pa-panel"></div>
<svg class="abs pa-notch" width="42" height="64"><polygon points="0,0 40,32 0,64" fill="#0c4f92"/></svg>
<div class="abs pa-bar"></div>
<div class="abs pa-title">PRACTICES<br>AREAS</div>
<div class="abs pa-copy">My law practice is dedicated to providing accessible legal services in trust, estate, probate, and guardianship administration and litigation, along with essential estate planning for everyday individuals and families. I focus on helping clients navigate the complexities of managing and distributing assets, ensuring that their loved ones are cared for and their wishes are respected</div>
<div class="abs pa-btn">SCHEDULE A<br>CONSULTATION</div>

<div class="abs pa-card" style="left:475px;top:1760px">
  <div class="photo" role="img" aria-label="Hands signing trust documents at a desk" style="inset:0;background:linear-gradient(160deg,#8b6a4e,#d8d2c6 55%,#b79c7c)"></div>
  <div class="pa-label">PROBATE AND<br>TRUSTS<span class="go"><svg width="14" height="14" viewBox="0 0 14 14"><path d="M2 7h10M8 3l4 4-4 4" stroke="#fff" stroke-width="1.6" fill="none"/></svg></span></div>
</div>
<div class="abs pa-card" style="left:816px;top:1760px">
  <div class="photo" role="img" aria-label="Older man and woman reviewing papers together" style="inset:0;background:linear-gradient(160deg,#d9cfc2,#7f7d7a 55%,#3a3b40)"></div>
  <div class="pa-label">ADULT<br>GUARDIANSHIPS<span class="go"><svg width="14" height="14" viewBox="0 0 14 14"><path d="M2 7h10M8 3l4 4-4 4" stroke="#fff" stroke-width="1.6" fill="none"/></svg></span></div>
</div>
<div class="abs pa-card" style="left:475px;top:2127px">
  <div class="photo" role="img" aria-label="Couple planning their estate with a small house model" style="inset:0;background:linear-gradient(160deg,#a8a39b,#6b6a60 55%,#c9c2b6)"></div>
  <div class="pa-label">ESTATE<br>PLANNING<span class="go"><svg width="14" height="14" viewBox="0 0 14 14"><path d="M2 7h10M8 3l4 4-4 4" stroke="#fff" stroke-width="1.6" fill="none"/></svg></span></div>
</div>
<div class="abs pa-card" style="left:816px;top:2127px">
  <div class="photo" role="img" aria-label="Judge's gavel on a desk in front of a lawyer" style="inset:0;background:linear-gradient(160deg,#c8c8c8,#5a4032 55%,#2e2522)"></div>
  <div class="pa-label">CIVIL<br>LITIGATION<span class="go"><svg width="14" height="14" viewBox="0 0 14 14"><path d="M2 7h10M8 3l4 4-4 4" stroke="#fff" stroke-width="1.6" fill="none"/></svg></span></div>
</div>

<!-- blog -->
<div class="abs bar blog-bar"></div>
<div class="abs blog-title">OUR BLOG</div>
<div class="abs blog-kicker">NEWS &amp; UPDATES</div>
<div class="abs arrow" style="left:1007px;top:2694px;background:#b7c2d6"><svg width="24" height="14" viewBox="0 0 24 14"><path d="M22 7H2M8 1 2 7l6 6" stroke="#fff" stroke-width="2" fill="none"/></svg></div>
<div class="abs arrow" style="left:1075px;top:2694px;background:var(--navy)"><svg width="24" height="14" viewBox="0 0 24 14"><path d="M2 7h20M16 1l6 6-6 6" stroke="#fff" stroke-width="2" fill="none"/></svg></div>

<article class="abs post" style="left:68px">
  <div class="img" role="img" aria-label="Team of professionals shaking hands in an office" style="background:linear-gradient(150deg,#d4d6d8,#8e8c88 60%,#3f4247)"></div>
  <div class="meta"><i></i>SEP 29, 2025</div>
  <h4>Trusts vs. Wills</h4>
  <p>Lorem ipsum dolor sit amet, con nsect ur adipiscing elit, sed do</p>
  <span class="more">READ MORE</span>
</article>
<article class="abs post" style="left:435px">
  <div class="img" role="img" aria-label="Two businessmen reviewing a tablet outside a building" style="background:linear-gradient(150deg,#e0e0de,#9a9790 55%,#2d2f34)"></div>
  <div class="meta"><i></i>SEP 21, 2025</div>
  <h4>Why probate is needed,... sometimes</h4>
  <p>When individuals think about estate planning,</p>
  <span class="more">READ MORE</span>
</article>
<article class="abs post" style="left:803px">
  <div class="img" role="img" aria-label="Hands gesturing over documents in a blue folder" style="background:linear-gradient(150deg,#3a4558,#c9c7c3 55%,#1f4f8f)"></div>
  <div class="meta"><i></i>SEP 29, 2025</div>
  <h4>Estate Planning Essentials</h4>
  <p>Lorem ipsum dolor sit amet, con nsect ur adipiscing elit, sed do</p>
  <span class="more">READ MORE</span>
</article>

<!-- schedule -->
<div class="abs bar sch-bar"></div>
<div class="abs sch-title">SCHEDULE A CONSULTATION OR<br>APPOINTMENT TODAY</div>
<div class="abs field" style="left:70px;top:3676px;width:292px;height:48px">First Name</div>
<div class="abs field" style="left:391px;top:3676px;width:292px;height:48px">Last Name</div>
<div class="abs field" style="left:70px;top:3750px;width:292px;height:47px">Phone</div>
<div class="abs field" style="left:391px;top:3750px;width:292px;height:47px">Email</div>
<div class="abs field" style="left:70px;top:3820px;width:613px;height:135px">Message</div>
<div class="abs btn-navy" style="left:68px;top:3994px;width:128px;height:46px;font-size:14px">SUBMIT</div>
<div class="abs sch-photo" role="img" aria-label="Two people shaking hands over a desk with legal papers" style="background:linear-gradient(160deg,#6d4a3c,#3a2722 50%,#1d1513)"><div class="inner"></div></div>

<!-- newsletter -->
<div class="abs news-title">NEWSLETTER SIGN UP</div>
<div class="abs news-sub">We Will Notify You Of Any Important News</div>
<div class="abs news-box"><span class="ph">ENTER YOUR EMAIL ADDRESS</span><span class="go">SUBSCIBE</span></div>

<!-- footer -->
<footer class="abs footer">
  <div class="footer-rule" style="left:0;width:360px"></div>
  <div class="footer-rule" style="left:838px;width:362px"></div>
  <div class="f-head" style="left:250px">QUICK LINKS</div>
  <div class="f-head" style="left:838px">CONTACT US</div>
  <ul class="f-links"><li>Home</li><li>About Us</li><li>Practice Area</li><li>Blog</li><li>Contact</li></ul>
  <div class="f-brand">KORVATCH LAW</div>
  <div class="f-contact">
    <div class="row"><span class="ic"><svg width="12" height="12" viewBox="0 0 24 24"><path fill="#fff" d="M6.6 10.8a15 15 0 0 0 6.6 6.6l2.2-2.2c.3-.3.7-.4 1-.2 1.1.4 2.3.6 3.6.6.6 0 1 .4 1 1V20c0 .6-.4 1-1 1A17 17 0 0 1 3 4c0-.6.4-1 1-1h3.5c.6 0 1 .4 1 1 0 1.3.2 2.5.6 3.6.1.3 0 .7-.2 1z"/></svg></span><div>CALL US<br>(555) 014-2290</div></div>
    <div class="row"><span class="ic"><svg width="12" height="12" viewBox="0 0 24 24"><circle cx="12" cy="12" r="10" fill="#fff"/><path d="M12 6v6l4 2" stroke="#0c4f92" stroke-width="2" fill="none"/></svg></span><div>WORKING HOURS<br>Mon - Fri 8AM - 5PM</div></div>
    <div class="row"><span class="ic"><svg width="12" height="14" viewBox="0 0 24 28"><path fill="#fff" d="M12 0a10 10 0 0 0-10 10c0 7.5 10 18 10 18s10-10.5 10-18A10 10 0 0 0 12 0zm0 14a4 4 0 1 1 0-8 4 4 0 0 1 0 8z"/></svg></span><div>240 Harlow Avenue Suite B<br>Marlowe, Texas 77000</div></div>
  </div>
</footer>
<div class="abs copyright">© 2025 Korvatch Law, PLLC | All Rights Reserved</div>

</body>
</html>
```